Veltarum

Standard Business Card design.
Sample two-sided design uploaded. White front, Black back.
Would like white shield to be on all black background side.
Willing to look at a couple creative designs, but nothing crazy.
Preference for a classic, confident, strong design.

```html
<!DOCTYPE html>
<html lang="en">
<head>
<meta charset="utf-8">
<title>Veltarum Business Card</title>
<link href="https://fonts.googleapis.com/css2?family=Poppins:wght@400;600;700&display=swap" rel="stylesheet">
<style>
  :root {
    --backdrop: #5c5c5c;
    --card-black: #000000;
    --card-white: #ffffff;
    --ink-light: #ffffff;
    --ink-dark: #111111;
  }
  html, body {
    margin: 0;
    padding: 0;
    width: 1200px;
    height: 1015px;
    overflow: hidden;
    background: var(--backdrop);
    font-family: "Poppins", sans-serif;
  }
  .sheet {
    width: 1200px;
    height: 1015px;
    display: flex;
    flex-direction: column;
    align-items: center;
    justify-content: center;
    gap: 40px;
  }
  .card {
    width: 800px;
    height: 457px;
    box-shadow: 0 14px 30px rgba(0,0,0,0.45);
    position: relative;
    overflow: hidden;
  }
  .card--back {
    background: var(--card-black);
    display: flex;
    align-items: center;
    justify-content: center;
  }
  .brand-name {
    font-weight: 700;
    letter-spacing: 0.12em;
    text-transform: uppercase;
    margin: 0;
  }
  .card--back .brand-name {
    color: var(--ink-light);
    font-size: 64px;
  }
  .card--front {
    display: flex;
  }
  .front-brand {
    width: 46%;
    background: var(--card-white);
    display: flex;
    flex-direction: column;
    align-items: center;
    justify-content: center;
  }
  .front-brand .brand-name {
    color: var(--ink-dark);
    font-size: 46px;
  }
  .front-brand .brand-rule {
    width: 250px;
    height: 2px;
    background: var(--ink-dark);
    margin-top: 10px;
  }
  .front-details {
    flex: 1;
    background: var(--card-black);
    color: var(--ink-light);
    padding: 70px 40px 0 56px;
    box-sizing: border-box;
  }
  .person-name {
    font-size: 26px;
    font-weight: 700;
    margin: 0;
    line-height: 1.1;
    text-transform: uppercase;
  }
  .person-role {
    font-size: 17px;
    margin: 2px 0 28px;
  }
  .contact-list {
    list-style: none;
    margin: 0 0 28px;
    padding: 0;
  }
  .contact-list li {
    display: flex;
    align-items: center;
    gap: 12px;
    font-size: 18px;
    line-height: 1.55;
  }
  .contact-list svg {
    width: 16px;
    height: 16px;
    flex: none;
  }
  .address {
    font-size: 18px;
    line-height: 1.35;
    margin: 0;
  }
</style>
</head>
<body>
<main class="sheet">
  <section class="card card--back">
    <p class="brand-name">Veltarum</p>
  </section>

  <section class="card card--front">
    <div class="front-brand">
      <p class="brand-name">Veltarum</p>
      <div class="brand-rule"></div>
    </div>
    <div class="front-details">
      <h1 class="person-name">Marcus Ellery</h1>
      <p class="person-role">Managing Director</p>
      <ul class="contact-list">
        <li>
          <svg viewBox="0 0 16 16" aria-hidden="true"><path d="M4 1.5l2.2 3-1.3 1.5c.8 1.8 2.3 3.3 4.1 4.1l1.5-1.3 3 2.2-1.3 2.5C7 13.5 2.5 9 2 2.8z" fill="#fff"/></svg>
          044-987 654 321
        </li>
        <li>
          <svg viewBox="0 0 16 16" aria-hidden="true"><rect x="1" y="3" width="14" height="10" fill="#fff"/><path d="M1 3l7 6 7-6" stroke="#000" stroke-width="1.3" fill="none"/></svg>
          info@veltarumgroup.com
        </li>
        <li>
          <svg viewBox="0 0 16 16" aria-hidden="true"><circle cx="8" cy="8" r="7" fill="#fff"/><g stroke="#000" stroke-width="1" fill="none"><ellipse cx="8" cy="8" rx="3" ry="7"/><path d="M1 8h14M2.5 4.5h11M2.5 11.5h11"/></g></svg>
          www.veltarumgroup.com
        </li>
      </ul>
      <p class="address">421, Address line goes here<br>45452, Country Name</p>
    </div>
  </section>
</main>
</body>
</html>
```